New letterhead design for legal, public interest law firm

THIS IS FOR A LETTERHEAD DESIGN CONTEST , PLEASE REFRAIN FROM SUBMITTING JUST LOGO PROPOSALS AND BUSINESS CARD. LOGO AND BUSINESS CARD PROJECTS WILL BE AWARDED TO THE WINNER OF THE LETTERHEAD DESIGN.
Looking for a timeless, elegant and modern design for our letterhead and logo. Our website is www.hlrbvwn.org so you can incorporate the mission, vision and values into the design. As we also included a request for a NEW LOGO design, please be sure to include logo design options.
We are a public interest criminal defense organization that represents indigent people charged with federal crimes. Please weave the mission/vision/values and our practice area into the logo design.
Target Market(s)
Judges, clients, attorneys, family members of our clients.
Industry/Entity Type
Legal
Contact Information for Business Card
Include line for address, direct line, fax, email address, website address. Remember to incorporate NEW LOGO design.
Logo Text
Harbor Legal Advocates Northern Bureau of Westmoor
Requirements
Must have
- Please remember this project is also to design us a NEW LOGO. Please do not incorporate the existing logo into the new letterhead design.
Nice to have
- Nice to see some logo samples incorporating symbolism for justice, California specific imagery.
Should not have
- New logo should NOT have any traditional/typical legal related images (e.g., scales of justice, etc.)

```html
<!DOCTYPE html>
<html lang="en">
<head>
<meta charset="utf-8">
<title>Harbor Legal Advocates — Stationery</title>
<link rel="stylesheet" href="https://fonts.googleapis.com/css2?family=Open+Sans:wght@400;600;700&display=swap">
<style>
:root{
  --blue:#0d4fa3;
  --orange:#f08a1c;
  --ink:#3a3a3a;
  --paper:#ffffff;
  --ground:#ebe4d8;
  --tint:#eef0f6;
}
*{margin:0;padding:0;box-sizing:border-box}
html,body{width:1200px;height:800px;overflow:hidden;background:var(--ground)}
body{position:relative;font-family:"Open Sans",Arial,sans-serif;color:var(--ink)}
.sheet{position:absolute;background:var(--paper);overflow:hidden;box-shadow:0 1px 3px rgba(0,0,0,.12)}
.brand{font-family:"Open Sans",Arial,sans-serif;font-weight:700;color:var(--blue);text-transform:uppercase;letter-spacing:.06em;line-height:1.25;display:flex;align-items:center;gap:5px}
.brand-mark{display:block;background:var(--blue);flex:none}
.bars{position:absolute;left:0;right:0;bottom:0}

/* business card front */
.card-front{left:27px;top:38px;width:236px;height:134px}
.card-front .brand{position:absolute;right:9px;top:10px;font-size:5.6px}
.card-front .brand-mark{width:14px;height:14px}
.holder{position:absolute;left:8px;top:70px}
.holder-name{font-size:9.5px;font-weight:600;color:var(--blue);letter-spacing:.04em}
.holder-role{font-size:5px;color:var(--blue);letter-spacing:.08em;display:flex;align-items:center;gap:4px;margin-top:1px}
.holder-role::after{content:"";width:18px;height:.6px;background:var(--blue)}
.card-contacts{position:absolute;left:8px;top:94px;list-style:none;font-size:4.8px;line-height:8px}
.card-contacts li{display:flex;align-items:center;gap:4px}
.card-contacts .web{color:var(--orange)}
.ico{width:6px;height:6px;flex:none}
.card-address{position:absolute;left:143px;top:115px;font-size:4.8px;line-height:6.6px}

/* business card back */
.card-back{left:27px;top:185px;width:236px;height:134px}
.card-back-ground{position:absolute;inset:0;background:linear-gradient(135deg,#f7f8fb,var(--tint))}
.card-back .brand{position:absolute;left:62px;top:52px;font-size:7.6px}
.card-back .brand-mark{width:22px;height:22px}
.card-back-line{position:absolute;left:0;right:0;bottom:9px;text-align:center;font-size:4.6px;font-weight:700;color:var(--orange)}

/* letterhead */
.letterhead{left:400px;top:106px;width:400px;height:567px}
.lh-header{position:absolute;left:45px;top:17px;width:317px;height:45px;border-bottom:1.6px solid var(--blue)}
.lh-header .brand{position:absolute;left:0;top:3px;font-size:8.2px}
.lh-header .brand-mark{width:26px;height:26px}
.lh-contacts{position:absolute;left:193px;top:0;list-style:none;font-size:6.6px;line-height:10.6px}
.lh-contacts li{display:flex;align-items:center;gap:6px}
.lh-contacts .ico{width:8px;height:8px}
.lh-contacts .web b{font-weight:400;color:var(--blue)}
.recipient{position:absolute;left:45px;top:97px;font-size:7.8px;line-height:12.2px}
.recipient-name{font-weight:700}
.recipient b{color:var(--blue);display:inline-block;width:14px}
.letter-date{position:absolute;right:40px;top:149px;font-size:6.4px}
.salutation{position:absolute;left:45px;top:160px;font-size:8px;font-weight:700}
.letter-body{position:absolute;left:45px;top:193px;width:317px;font-size:8px;line-height:12.2px;text-align:justify}
.letter-body p{margin-bottom:12.2px}
.signature{position:absolute;left:37px;top:455px;width:112px;height:36px;background:linear-gradient(90deg,rgba(58,58,58,.08),rgba(58,58,58,.18),rgba(58,58,58,.06));border-radius:3px}
.signer{position:absolute;left:46px;top:490px;font-size:8px;line-height:12px}
.signer-name{font-weight:700}

/* envelopes */
.env-front{left:813px;top:251px;width:366px;height:184px}
.env-front-flap{position:absolute;left:0;top:0;width:366px;height:25px}
.env-front .brand{position:absolute;left:130px;top:80px;font-size:7px}
.env-front .brand-mark{width:26px;height:26px}
.env-back{left:823px;top:478px;width:363px;height:181px;background:transparent;box-shadow:none}
.env-back-body{position:absolute;inset:0}
.env-back .brand{position:absolute;left:12px;top:128px;font-size:6.2px}
.env-back .brand-mark{width:22px;height:22px}
.env-address{position:absolute;left:12px;top:155px;font-size:5.4px;line-height:6.6px;font-weight:600;color:var(--blue);letter-spacing:.05em}
</style>
</head>
<body>

<!-- business card front -->
<section class="sheet card-front" aria-label="Business card front">
  <div class="brand"><span class="brand-mark"></span><span>Harbor Legal Advocates<br>Northern Bureau of Westmoor</span></div>
  <div class="holder">
    <p class="holder-name">Daniel J. Morrow</p>
    <p class="holder-role">CEO</p>
  </div>
  <ul class="card-contacts">
    <li><svg class="ico" viewBox="0 0 10 10"><rect width="10" height="10" fill="#0d4fa3"/><path d="M3 2.2l1.2 1.6-.7.8c.5 1 1.2 1.7 2.2 2.2l.8-.7 1.6 1.2-.7 1.2C5 8.3 1.9 5.2 2 3z" fill="#fff"/></svg>+1 555 014 2268</li>
    <li><svg class="ico" viewBox="0 0 10 10"><rect width="10" height="10" fill="#0d4fa3"/><rect x="2.5" y="4" width="5" height="3" fill="#fff"/><rect x="3.3" y="2" width="3.4" height="2" fill="#fff"/></svg>(555) 019.4410</li>
    <li><svg class="ico" viewBox="0 0 10 10"><rect width="10" height="10" fill="#0d4fa3"/><rect x="2" y="3" width="6" height="4" fill="#fff"/><path d="M2 3l3 2.3L8 3" stroke="#0d4fa3" stroke-width=".7" fill="none"/></svg>contact@hlrbvwn.org</li>
    <li class="web"><svg class="ico" viewBox="0 0 10 10"><rect width="10" height="10" fill="#0d4fa3"/><circle cx="5" cy="5" r="2.8" stroke="#fff" stroke-width=".7" fill="none"/><path d="M2.2 5h5.6M5 2.2v5.6" stroke="#fff" stroke-width=".6"/></svg>www.hlrbvwn.org</li>
  </ul>
  <p class="card-address">412 Tidewater Ln;<br>Westmoor, WM 40112-3381</p>
  <svg class="bars" width="236" height="2" viewBox="0 0 236 2" preserveAspectRatio="none"><polygon points="0,0 117,0 119,2 0,2" fill="#0d4fa3"/><polygon points="119,0 236,0 236,2 121,2" fill="#f08a1c"/></svg>
</section>

<!-- business card back -->
<section class="sheet card-back" aria-label="Business card back">
  <div class="card-back-ground" role="img" aria-label="Soft repeating brand pattern"></div>
  <div class="brand"><span class="brand-mark"></span><span>Harbor Legal Advocates<br>Northern Bureau of Westmoor</span></div>
  <p class="card-back-line">Harbor Legal Advocates Northern Bureau of Westmoor</p>
</section>

<!-- letterhead -->
<article class="sheet letterhead" aria-label="Letterhead">
  <header class="lh-header">
    <div class="brand"><span class="brand-mark"></span><span>Harbor Legal Advocates<br>Northern Bureau<br>of Westmoor</span></div>
    <ul class="lh-contacts">
      <li><svg class="ico" viewBox="0 0 10 10"><rect width="10" height="10" fill="#0d4fa3"/><path d="M5 1.8a2.3 2.3 0 0 1 2.3 2.3C7.3 5.8 5 8.3 5 8.3S2.7 5.8 2.7 4.1A2.3 2.3 0 0 1 5 1.8z" fill="#fff"/><circle cx="5" cy="4.1" r=".9" fill="#0d4fa3"/></svg>18/B, Quay Street, Westmoor</li>
      <li><svg class="ico" viewBox="0 0 10 10"><rect width="10" height="10" fill="#0d4fa3"/><path d="M3 2.2l1.2 1.6-.7.8c.5 1 1.2 1.7 2.2 2.2l.8-.7 1.6 1.2-.7 1.2C5 8.3 1.9 5.2 2 3z" fill="#fff"/></svg>+1 555 014 2268</li>
      <li><svg class="ico" viewBox="0 0 10 10"><rect width="10" height="10" fill="#0d4fa3"/><rect x="2" y="3" width="6" height="4" fill="#fff"/><path d="M2 3l3 2.3L8 3" stroke="#0d4fa3" stroke-width=".7" fill="none"/></svg>contact@hlrbvwn.org</li>
      <li class="web"><svg class="ico" viewBox="0 0 10 10"><rect width="10" height="10" fill="#0d4fa3"/><circle cx="5" cy="5" r="2.8" stroke="#fff" stroke-width=".7" fill="none"/><path d="M2.2 5h5.6M5 2.2v5.6" stroke="#fff" stroke-width=".6"/></svg><span>www.<b>hlrbvwn</b>.org</span></li>
    </ul>
  </header>

  <address class="recipient" style="font-style:normal">
    <p class="recipient-name">BRAMBLEWICK GROUP,LLC</p>
    <p><b>A</b>: 27-3, Larkfield Road Eastvale - 5120</p>
    <p><b>W</b>: www.BramblewickGroupLLC.com</p>
    <p><b>P</b>: +1 - 55501 - 7734</p>
  </address>
  <p class="letter-date">Date, 10 September, 2020</p>
  <p class="salutation">Dear, Johns</p>

  <div class="letter-body">
    <p>Contrary to popular belief, Lorem Ipsum is not simply random text. It has roots in a piece of classical Latin literature from 45 BC, making it over 2000 years old. Richard Castellane, a Latin professor at Ashbourne College in Virginia, looked up one of the more obscure Latin words, consectetur, from a Lorem Ipsum passage, and going through the cites of the word in classical literature, discovered the undoubtable source.</p>
    <p>Lorem Ipsum comes from sections 1.10.32 and 1.10.33 of "de Finibus Bonorum et Malorum" (The Extremes of Good and Evil) by Corvinus, written in 45 BC. This book is a treatise on the theory of ethics, very popular during the Renaissance. Lorem Ipsum used since the 1500s is reproduced below for those interested. Sections 1.10.32 and 1.10.33 from "de Finibus Bonorum et Malorum" by Corvinus are also reproduced in their exact original form, accompanied by English versions from the 1914 translation by H. Ravenscroft.</p>
    <p>Contrary to popular belief, Lorem Ipsum is not simply random text. It has roots in a piece of classical Latin literature from 45 BC, making it over 2000 years old. Richard Castellane, a Latin professor at Ashbourne College in Virginia, looked up one of the more obscure Latin words.</p>
  </div>

  <div class="signature" role="img" aria-label="Handwritten signature"></div>
  <div class="signer">
    <p class="signer-name">Walter K. Ashford</p>
    <p>General Director</p>
  </div>

  <svg class="bars" width="400" height="6" viewBox="0 0 400 6" preserveAspectRatio="none"><polygon points="0,0 244,0 249,6 0,6" fill="#0d4fa3"/><polygon points="250,0 400,0 400,6 255,6" fill="#f08a1c"/></svg>
</article>

<!-- envelope front -->
<section class="sheet env-front" aria-label="Envelope front">
  <svg class="env-front-flap" viewBox="0 0 366 25" preserveAspectRatio="none"><polygon points="0,0 366,0 342,25 24,25" fill="#0d4fa3"/></svg>
  <div class="brand"><span class="brand-mark"></span><span>Harbor Legal Advocates<br>Northern Bureau of Westmoor</span></div>
</section>

<!-- envelope back -->
<section class="sheet env-back" aria-label="Envelope back">
  <svg class="env-back-body" viewBox="0 0 363 181" preserveAspectRatio="none">
    <rect width="363" height="181" fill="#fff"/>
    <path d="M0,0 H363 L360,42 Q358,48 350,48 L181,67 L12,48 Q4,48 3,42 Z" fill="#0d4fa3"/>
    <polygon points="0,178 195,178 197,181 0,181" fill="#0d4fa3"/>
    <polygon points="197,178 363,178 363,181 199,181" fill="#f08a1c"/>
  </svg>
  <div class="brand"><span class="brand-mark"></span><span>Harbor Legal Advocates<br>Northern Bureau of Westmoor</span></div>
  <p class="env-address">7720 Harbor Crest Dr; Westmoor,<br>WM 40118-2257</p>
</section>

</body>
</html>
```